Web design required

1-We need a web design for existing company based in New Zealand
2-We build residential house and light commercial
3-We has in-house designer which allow us can provide interior design
4-We modeling project before site construction, which enable both client and construction team to visually analysis whole project,

Target Market(s)

middle class residential house market
Ref: http://www.brambleworthbuilders.co.nz/

Industry/Entity Type

Construction Company

Number of Pages Required

1 page

Font styles to use
Sans Serif
Other font styles liked:
• Such as : Central Gothic or similar which has more design taste

Colors

Designer to choose colors to be used in the design.

Requirements
Must have
• Front sheet, contact information, sample project

```html
<!DOCTYPE html>
<html lang="en">
<head>
<meta charset="utf-8">
<title>Kauri Ridge Homes</title>
<link href="https://fonts.googleapis.com/css2?family=Montserrat:wght@500;600;700&family=Open+Sans:wght@400;600&family=Raleway:wght@400;600&family=Roboto:wght@400;500;700&display=swap" rel="stylesheet">
<style>
:root{
  --blue:#3b6fd8;
  --navy:#123d7a;
  --green:#3cb54a;
  --lime:#39b54a;
  --ink:#1e1e1e;
  --body:#555;
  --light:#f2f2f2;
  --footer:#262626;
  --footer-text:#9a9a9a;
  --white:#fff;
}
*{margin:0;padding:0;box-sizing:border-box}
html,body{width:1200px;height:3727px;overflow:hidden}
body{position:relative;background:var(--white);font-family:'Open Sans',sans-serif;color:var(--body)}
.abs{position:absolute}
.fill{display:block}

/* header */
.site-header{left:0;top:0;width:1200px;height:95px;background:var(--white)}
.brand{left:110px;top:22px;display:flex;align-items:center;gap:14px}
.brand-mark{width:46px;height:46px;background:var(--blue);border-radius:50%}
.brand-name{font-family:'Montserrat',sans-serif;font-weight:600;font-size:22px;letter-spacing:4px;color:var(--navy);line-height:1.05}
.main-nav{left:492px;top:46px;display:flex;gap:40px;font-family:'Roboto',sans-serif;font-size:16px;font-weight:500;color:var(--ink)}
.main-nav a{color:inherit;text-decoration:none;position:relative}
.main-nav a.active::after{content:"";position:absolute;left:0;right:0;bottom:-16px;height:3px;background:var(--green)}
.user-btn{left:1048px;top:48px;width:24px;height:24px;background:#1e88e5}

/* hero */
.hero{left:0;top:95px;width:1200px;height:583px;background:linear-gradient(160deg,#3a3b40 0%,#25262b 45%,#1d2330 70%,#2b3342 100%)}
.hero-tag{left:1046px;top:112px;width:26px;height:22px;background:var(--lime)}
.hero-title{left:142px;top:272px;display:flex;height:76px}
.hero-title .t1{width:581px;background:var(--white);font-family:'Roboto',sans-serif;font-weight:500;font-size:33px;color:#222;display:flex;align-items:center;justify-content:center}
.hero-title .t2{width:308px;background:var(--navy);font-family:'Roboto',sans-serif;font-weight:700;font-size:40px;color:var(--green);display:flex;align-items:center;justify-content:center}
.hero-sub{left:0;top:376px;width:1200px;text-align:center;font-family:'Raleway',sans-serif;font-size:26px;color:var(--white)}
.hero-btn{left:460px;top:447px;width:278px;height:62px;background:var(--green);color:var(--white);font-family:'Roboto',sans-serif;font-size:22px;display:flex;align-items:center;justify-content:center}

/* offer */
.section-title{left:0;width:1200px;text-align:center;font-family:'Montserrat',sans-serif;font-weight:600;font-size:40px;color:#111}
.section-sub{left:0;width:1200px;text-align:center;font-family:'Raleway',sans-serif;font-weight:600;font-size:18px;color:#333}
.offer-text{left:145px;top:858px;width:910px;text-align:center;font-size:15px;line-height:24px;color:#555}
.showcase{left:100px;top:1013px;width:1000px;height:361px}
.showcase-cap{left:100px;top:1306px;width:1000px;text-align:center;color:var(--white)}
.showcase-cap b{display:block;font-family:'Montserrat',sans-serif;font-size:19px;letter-spacing:2px}
.showcase-cap span{font-size:14px}

/* about */
.skyline{left:0;top:1466px;width:1200px;height:150px}
.about{left:0;top:1615px;width:1200px;height:489px;background:var(--blue)}
.about-photo{left:596px;top:1590px;width:604px;height:514px}
.about-copy{left:114px;top:1696px;width:470px;color:var(--white)}
.kicker{font-family:'Montserrat',sans-serif;font-size:11px;font-weight:700;letter-spacing:1px}
.about-copy h2{font-family:'Montserrat',sans-serif;font-weight:700;font-size:27px;letter-spacing:1px;margin:4px 0 8px}
.lead{font-size:11px;font-weight:600;line-height:16px;text-transform:uppercase}
.about-copy p.body{font-size:11px;line-height:17px;margin-top:10px}
.features{list-style:none;margin-top:18px;font-size:10.5px;font-weight:600;text-transform:uppercase;line-height:21px}
.features li::before{content:"✓";margin-right:12px}
.outline-btn{left:134px;top:1980px;width:117px;height:32px;border:1px solid var(--white);color:var(--white);font-size:12px;display:flex;align-items:center;justify-content:center}

/* portfolio */
.tile{overflow:hidden}
.tile-bar{position:absolute;left:0;bottom:0;width:100%;background:rgba(0,0,0,.85);color:var(--white);padding:8px 14px}
.tile-bar b{display:block;font-family:'Montserrat',sans-serif;font-weight:600;font-size:28px;line-height:32px}
.tile-bar span{font-size:12px}
.tile-bar i{font-style:normal;color:var(--green)}

/* testimonial */
.video{left:99px;top:2996px;width:475px;height:283px}
.clients-title{left:599px;top:2994px;font-family:'Montserrat',sans-serif;font-weight:600;font-size:21px;color:#222}
.quote{left:599px;top:3043px;width:474px;height:122px;background:var(--light);padding:20px 22px;font-size:11.5px;line-height:19px;color:#666}
.avatar{left:599px;top:3194px;width:66px;height:66px;border-radius:50%}
.author{left:683px;top:3196px}
.author b{display:block;font-family:'Roboto',sans-serif;font-weight:500;font-size:16px;color:#222}
.author span{font-size:12px;color:#888}
.author .stars{color:#f5a623;font-size:13px;display:block;margin-top:2px;letter-spacing:1px}

/* footer */
.site-footer{left:0;top:3361px;width:1200px;height:366px;background:var(--footer);color:var(--footer-text)}
.foot-brand{left:99px;top:3413px;display:flex;align-items:center;gap:12px}
.foot-brand .brand-mark{width:40px;height:40px;background:#888}
.foot-brand .brand-name{color:#999;font-size:18px}
.foot-about{left:99px;top:3490px;width:215px;font-size:12px;line-height:18px}
.socials{left:99px;top:3580px;display:flex;gap:10px}
.socials span{width:28px;height:28px;border-radius:50%;background:#555}
.foot-col{top:3392px;font-size:12px}
.foot-col h4{font-family:'Montserrat',sans-serif;font-size:13px;font-weight:700;color:var(--white);letter-spacing:.5px;margin-bottom:30px}
.contact-list li{list-style:none;display:flex;gap:10px;margin-bottom:12px;line-height:16px}
.contact-list svg{flex:none;margin-top:2px}
.link-list li{list-style:none;margin-bottom:14px}
.link-list li::before{content:"›";margin-right:10px;color:#666}
.news p{width:230px;line-height:22px;margin-bottom:16px}
.news .field{width:230px;height:42px;border:1px solid #444;padding:12px 14px;color:#ccc}
.news .signup{width:230px;height:42px;margin-top:12px;background:#2979ff;color:var(--white);font-weight:600;display:flex;align-items:center;justify-content:center}
.copyright{left:0;top:3700px;width:1200px;text-align:center;font-size:12px;color:#888}
</style>
</head>
<body>

<header class="site-header abs">
  <div class="brand abs"><span class="brand-mark"></span><span class="brand-name">KAURI RIDGE<br>HOMES</span></div>
  <nav class="main-nav abs">
    <a class="active" href="#">Home</a><a href="#">Portfolio</a><a href="#">Services</a><a href="#">About</a><a href="#">Blog</a><a href="#">Contact</a>
  </nav>
  <div class="user-btn abs"></div>
</header>

<section class="hero abs" role="img" aria-label="Modern luxury home at dusk with lit terrace and swimming pool"></section>
<div class="hero-tag abs"></div>
<div class="hero-title abs"><div class="t1">High-End Residential Construction</div><div class="t2">SINCE 1995</div></div>
<p class="hero-sub abs">High Performance Homes Improved Comfort and Efficiency</p>
<a class="hero-btn abs">HOME FOR SALE &nbsp;›</a>

<h2 class="section-title abs" style="top:752px">What We Offer</h2>
<p class="section-sub abs" style="top:815px">Specialising in Kauri Ridge Homes</p>
<p class="offer-text abs">simply dummy text of the printing and typesetting industry. Lorem Ipsum has been the industry's standard dummy text ever since the 1500s, when an unknown printer took a galley of type and scrambled it to make a type specimen book. It has survived not only five centuries, but also the leap into electronic typesetting, remaining essentially unchanged. It was popularised in the 1960s with the release of Letraset sheets.</p>

<svg class="showcase abs" viewBox="0 0 1000 361" role="img" aria-label="Three photos of modern homes: a lit house at night, a patio at dusk and a home with a pool">
  <defs>
    <linearGradient id="g1" x1="0" y1="0" x2="0" y2="1"><stop offset="0" stop-color="#2d3440"/><stop offset="1" stop-color="#5a4a34"/></linearGradient>
    <linearGradient id="g2" x1="0" y1="0" x2="0" y2="1"><stop offset="0" stop-color="#3f63a8"/><stop offset="1" stop-color="#2a2e38"/></linearGradient>
    <linearGradient id="g3" x1="0" y1="0" x2="0" y2="1"><stop offset="0" stop-color="#2b3a55"/><stop offset=".6" stop-color="#7a5a3a"/><stop offset="1" stop-color="#1e8fb8"/></linearGradient>
  </defs>
  <polygon points="0,0 355,0 300,180 355,361 0,361" fill="url(#g1)"/>
  <polygon points="655,0 1000,0 1000,361 655,361 700,180" fill="url(#g3)"/>
  <polygon points="370,0 640,0 688,180 640,361 370,361 318,180" fill="url(#g2)"/>
</svg>
<div class="showcase-cap abs"><b>KAURI RIDGE</b><span>Specialising in Kauri Ridge Homes</span></div>

<div class="skyline abs" role="img" aria-label="Pale city skyline silhouette rising into the blue band" style="background:linear-gradient(#fff 0%,#e6ebf3 55%,var(--blue) 100%)"></div>
<section class="about abs"></section>
<div class="about-photo abs" role="img" aria-label="Hand holding a small model house with keys" style="background:linear-gradient(90deg,rgba(59,111,216,0) 0%,#c9a58a 45%,#e0c2a8 70%,#4a4f5a 100%)"></div>
<div class="about-copy abs">
  <div class="kicker">A FEW WORDS ABOUT HOUSE</div>
  <h2>SPECIALISING IN KAURI RIDGE</h2>
  <p class="lead">Lorem ipsum dolor sit amet, consectetur adipiscing elit. Ligula convallis, vel tincidunt ipsum posuere</p>
  <p class="body">Lorem ipsum dolor sit amet, consectetur adipiscing elit. Sed tempor arcu non ligula convallis, vel tincidunt ipsum posuere. Fusce sodales lacus ut pellentesque tincidunt. Duis iaculis, arcu ut hendrerit pharetra, elit augue pulvinar magna, a consectetur eros quam eu dui.</p>
  <ul class="features">
    <li>High efficiency central air &amp; heating</li>
    <li>Heated flooring on 1st and 2nd level</li>
    <li>New carpet in every room</li>
    <li>Smart refrigerator</li>
  </ul>
</div>
<a class="outline-btn abs">CONTACT US</a>

<h2 class="section-title abs" style="top:2164px">Our Portfolio</h2>
<div class="tile abs" style="left:107px;top:2280px;width:472px;height:472px" role="img" aria-label="Villa with indoor pool and open living area">
  <div class="fill" style="height:148px;background:linear-gradient(#2f5fa8,#cfdcec)"></div>
  <div class="fill" style="height:324px;background:linear-gradient(#3a3a3e,#7c8a94 60%,#4fa3c8)"></div>
  <div class="tile-bar"><b>Villa</b><span><i>8</i> Properties</span></div>
</div>
<div class="tile abs" style="left:609px;top:2280px;width:474px;height:224px;background:linear-gradient(#9fb4c8,#3a3d44)" role="img" aria-label="Modern apartment building">
  <div class="tile-bar"><b>Apartment</b><span><i>6</i> Properties</span></div>
</div>
<div class="tile abs" style="left:609px;top:2529px;width:223px;height:223px;background:linear-gradient(#e8a24a,#3a4a2a)" role="img" aria-label="House at sunset">
  <div class="tile-bar"><b>House</b><span><i>10</i> Properties</span></div>
</div>
<div class="tile abs" style="left:857px;top:2529px;width:226px;height:223px;background:linear-gradient(#c0d8ea,#8a6a4a)" role="img" aria-label="Farm house with garden">
  <div class="tile-bar"><b>Farm</b><span><i>1</i> Property</span></div>
</div>

<h2 class="section-title abs" style="top:2845px">What We Offer</h2>
<p class="section-sub abs" style="top:2910px">Specialising in Kauri Ridge Homes</p>
<div class="video abs" role="img" aria-label="Video still of a couple holding a house outline sign" style="background:linear-gradient(90deg,#5a5a5a,#8a7a78 50%,#6b4b4e)">
  <svg class="abs" style="left:210px;top:114px" width="54" height="54" viewBox="0 0 54 54"><circle cx="27" cy="27" r="25" fill="none" stroke="#fff" stroke-width="3"/><polygon points="21,16 39,27 21,38" fill="#fff"/></svg>
</div>
<h3 class="clients-title abs">2000+ Happy Clients</h3>
<p class="quote abs">The Tomlin Family recently sold our house and home. We have found that it was one of the best decisions we could have made, as nothing was a problem to her, and it certainly took the worry of marketing and selling off our mind, as the team had everything under control.</p>
<div class="avatar abs" role="img" aria-label="Client portrait" style="background:#d9c7b8"></div>
<div class="author abs"><b>Mara &amp; Theo</b><span>Hamilton, Waikato</span><span class="stars">★★★★★</span></div>

<footer class="site-footer abs"></footer>
<div class="foot-brand abs"><span class="brand-mark"></span><span class="brand-name">KAURI RIDGE<br>HOMES</span></div>
<p class="foot-about abs">Harbourline Ltd is a registered builder and Member of the Waikato Valley Builders Guild.</p>
<div class="socials abs"><span></span><span></span><span></span><span></span></div>

<div class="foot-col abs" style="left:355px">
  <h4>GET IN TOUCH</h4>
  <ul class="contact-list">
    <li><svg width="10" height="12" viewBox="0 0 10 12"><path d="M5 0a4 4 0 0 0-4 4c0 3 4 8 4 8s4-5 4-8a4 4 0 0 0-4-4z" fill="#2979ff"/></svg><span>18 Kowhai Lane, Hamilton 3204<br>New Zealand</span></li>
    <li><svg width="10" height="12" viewBox="0 0 10 12"><path d="M2 0l2 3-1 2c1 2 2 3 4 4l2-1 1 3-2 1C4 11 0 6 1 1z" fill="#2979ff"/></svg><span>(07) 555 0142</span></li>
    <li><svg width="10" height="12" viewBox="0 0 10 12"><path d="M0 6l10-5-3 10-2-4z" fill="#2979ff"/></svg><span>hello@kauriridgehomes.co.nz</span></li>
    <li><svg width="10" height="12" viewBox="0 0 10 12"><rect x="1" y="0" width="8" height="12" rx="1.5" fill="#2979ff"/></svg><span>(07) 555 0142</span></li>
    <li><svg width="10" height="12" viewBox="0 0 10 12"><circle cx="5" cy="6" r="4.5" fill="none" stroke="#2979ff" stroke-width="1.5"/></svg><span>Mon – Sat : 9:00 – 18:00</span></li>
  </ul>
</div>
<div class="foot-col abs" style="left:614px">
  <h4>INFORMATION</h4>
  <ul class="link-list"><li>Home</li><li>Services</li><li>Solutions</li><li>Resources</li><li>Career</li><li>Contact Us</li></ul>
</div>
<div class="foot-col news abs" style="left:869px">
  <h4>NEWS LETTER</h4>
  <p>Enter your email address for our mailing list to keep your self our latest updated.</p>
  <div class="field">Email</div>
  <div class="signup">Sign up</div>
</div>
<p class="copyright abs">Copyright © 2007 - 2017 Kauri Ridge Homes. All Rights Reserved</p>

</body>
</html>
```